Unternehmensvorstellung : Broschüre DIN A4 ca. 6 Innenseiten.
Zielgruppe
Dienstleistungen:
- Messdienst und Erstellung Heiz- und Nebenkostenabrechung für Mieter
- Rauchwarnmelder Montage und Wartung
- Trinkwasser/Legionellenprüfung
- Energie-Monitoring-Service (automatisch Ermittlung günstigster Versorger)
Für:
Immobilienverwalter
Immobilienbesitzer
Immobilien Gesellschaften
Architekten und Planer
Aufgabenstellung
siehe Homepage www.wohnarcaplus.de

```html
<!DOCTYPE html>
<html lang="de">
<head>
<meta charset="utf-8">
<title>Wartungs- und Ableseservice – Broschüre Doppelseite</title>
<link rel="stylesheet" href="https://fonts.googleapis.com/css2?family=Arimo:wght@400;700&family=Inter:wght@300;400&display=swap">
<style>
  :root {
    --slate: #334a58;
    --slate-light: #71838e;
    --paper: #ffffff;
    --ink: #3b4b55;
    --ink-soft: #55636c;
    --photo-dark: #5f6a72;
    --photo-mid: #a7adb2;
    --photo-light: #dfe1e3;
    --bg: #e6e6e6;
  }
  html, body { margin: 0; padding: 0; width: 1200px; height: 833px; overflow: hidden; background: var(--bg); }
  .spread { position: relative; width: 1200px; height: 833px; font-family: Arimo, Arial, sans-serif; }

  .page { position: absolute; top: 0; width: 600px; height: 833px; overflow: hidden; }
  .page--left { left: 0; }
  .page--right { left: 600px; }

  .page-photo { position: absolute; inset: 0; }
  .page--left .page-photo { background: linear-gradient(135deg, var(--photo-dark) 0%, var(--photo-mid) 45%, var(--photo-light) 80%, #c9cdd0 100%); }
  .page--right .page-photo { background: linear-gradient(160deg, var(--photo-mid) 0%, var(--photo-dark) 20%, var(--photo-light) 55%, #b9bec2 100%); }

  /* Left page */
  .service-panel {
    position: absolute; left: 36px; top: 44px; width: 524px; height: 752px;
    background: linear-gradient(110deg, var(--slate) 0%, var(--slate) 55%, var(--slate-light) 100%);
    color: #fff;
  }
  .service-title {
    position: absolute; left: 44px; top: 170px; margin: 0;
    font-family: Inter, Arial, sans-serif; font-weight: 300;
    font-size: 36px; line-height: 36px; letter-spacing: 1px; text-transform: uppercase;
  }
  .service-copy { position: absolute; left: 44px; top: 300px; width: 228px; font-size: 8.6px; line-height: 11.4px; }
  .service-copy p { margin: 0 0 9px; }
  .service-aside { position: absolute; left: 292px; top: 250px; width: 200px; font-size: 8.6px; line-height: 11.4px; }
  .service-aside p { margin: 12px 0 0; }

  .benefits { border: 1.5px solid currentColor; padding: 10px 12px 12px; font-size: 8.4px; line-height: 11px; }
  .benefits h3 { margin: 0 0 6px; font-size: 10px; font-weight: 400; letter-spacing: 1px; text-transform: uppercase; }
  .benefits ul { margin: 0; padding-left: 14px; }
  .benefits li { margin: 0 0 1px; }

  /* Right page */
  .methods-panel { position: absolute; left: 26px; top: 44px; width: 534px; height: 752px; background: var(--paper); color: var(--ink-soft); }
  .methods-text { position: absolute; left: 36px; top: 60px; width: 300px; font-size: 8.4px; line-height: 11.2px; }
  .method { margin-bottom: 30px; }
  .method h2 { margin: 0 0 8px; color: var(--slate); font-size: 11px; font-weight: 700; letter-spacing: 0.8px; text-transform: uppercase; line-height: 13px; }
  .method p { margin: 0; }

  .method-visual { position: absolute; left: 370px; width: 140px; text-align: center; }
  .method-visual .visual-area { width: 140px; height: 110px; background: linear-gradient(160deg, #f2f2f2 0%, #c9c9c9 60%, #9a9a9a 100%); }
  .method-visual .caption { margin-top: 5px; color: #222; font-size: 7px; font-weight: 700; line-height: 8.5px; text-transform: uppercase; }
  .visual--manual { top: 50px; }
  .visual--walkby { top: 235px; }
  .visual--remote { top: 420px; }

  .methods-benefits { position: absolute; left: 36px; top: 585px; width: 300px; color: var(--ink-soft); border-color: var(--slate); }
  .methods-benefits h3 { color: var(--slate); font-weight: 700; }
</style>
</head>
<body>
<div class="spread">

  <section class="page page--left">
    <div class="page-photo" role="img" aria-label="Unscharfes Hintergrundfoto in Grautönen"></div>
    <div class="service-panel">
      <h1 class="service-title">Wartungs- und<br>Ableseservice</h1>

      <div class="service-copy">
        <p>Unser Ablese- und Wartungs-Service garantiert die termingerechte Ablesung der Verbrauchsdaten und die sorgfältige Dokumentation aller Werte. Ganz klar: Nur wenn die Verbrauchsdaten regelmäßig und zuverlässig erfasst werden, können die Kosten gerecht auf die Nutzer verteilt werden.</p>
        <p>Daher überwachen wir die Ablesestichtage und unsere geschulten Servicepartner lesen die Verbrauchsdaten termingerecht ab. Je nach technischer Ausstattung der Liegenschaft geschieht dies entweder direkt am Mess-/Verteilgerät oder außerhalb der Nutzeinheit. Bevor wir in die Liegenschaft zum Ablesen kommen, informieren wir die Mieter frühzeitig, zu welchem Termin die Räume zugänglich gemacht werden sollten. Bei der Ablesung werden die Geräte, soweit vorgesehen und erforderlich, neu verplombt.</p>
        <p>Nach Prüfung der Daten auf Richtigkeit, Gerätezugehörigkeit und Plausibilität übernehmen wir sie dann in unseren Abrechnungsservice. Bei fehlenden oder unplausiblen Werten berechnen wir die Verbrauchswerte gemäß den gesetzlichen Vorschriften.</p>
        <p>Bei uns bekommen Sie bei manueller Ablesung einen Ablesebeleg.</p>
        <p>Während ihn andere Messdienstunternehmen abgeschafft haben, hielten wir am Ablesebeleg fest. Jetzt ist es durch die neue Heizkostenverordnung auch amtlich: Der Ablesebeleg ist wichtig! Er schafft für Mieter/Nutzer Transparenz und reduziert damit die Mieternachfragen. Außerdem ist er Bestandteil unserer rechtssicheren Dokumentation. Das sorgt für zufriedene Mieter und schützt Sie als Kunde vor unberechtigten Reklamationen.</p>
      </div>

      <div class="service-aside">
        <div class="benefits">
          <h3>Ihre Vorteile</h3>
          <ul>
            <li>Klare und nachvollziehbare Ablesung</li>
            <li>Einwandfreie Dokumentation durch Ablesebeleg mit allen wichtigen Daten</li>
            <li>Keine Manipulation bei der Ablesung möglich</li>
            <li>Schreibfehler bei der Ablesung sind ausgeschlossen</li>
            <li>Genauer Nachweis von Ablesedatum, Ablesezeit und Ablesername</li>
          </ul>
        </div>
        <p>Den Verbrauchsdatenservice führen wir durch, wann immer Sie ihn brauchen – ob zum vereinbarten Hauptablesetermin oder im Verlauf des Abrechnungszeitraumes, z.B. bei Nutzerwechseln im laufenden Abrechnungsjahr.</p>
      </div>
    </div>
  </section>

  <section class="page page--right">
    <div class="page-photo" role="img" aria-label="Unscharfes Hintergrundfoto in Silber- und Grautönen"></div>
    <div class="methods-panel">
      <div class="methods-text">
        <article class="method">
          <h2>Manuelle Ablesung</h2>
          <p>Bei der manuellen Ablesung erfolgt die Erfassung der Verbrauchswerte mit einem mobilen Datenerfassungsgerät direkt am Mess-/Verteilgerät. Bei allen elektronischen Geräten werden die Verbrauchswerte mittels einer optischen Schnittstelle elektronisch ausgelesen. Bei allen nicht elektronischen Geräten erfolgt eine manuelle Ablesung der Verbrauchswerte. Dieses Verfahren eignet sich besonders für kleine Liegenschaften, in der die einzelnen Geräte leicht zugänglich sind. Mit der mobilen Datenerfassung können potenzielle Fehlerquellen minimiert und kann eine hohe Datensicherheit gewährleistet werden.</p>
        </article>
        <article class="method">
          <h2>Walk-by / halbautomatische Ablesung</h2>
          <p>Alle Werte werden komplett an einer zentralen Stelle der Liegenschaft abgelesen – ohne Betreten einzelner Nutzeinheiten. Diese Art der Verbrauchserfassung wird durch zwei Systeme ermöglicht: Einerseits können die Daten drahtlos per Funktechnologie an einen mobilen Datenerfassungsgerät oder eine Gebäudezentrale übertragen werden. Andererseits besteht die Möglichkeit, diese kabelgebunden per M-Bus zu ermitteln. Besonders bei mittelgroßen Liegenschaften reduziert sich bei diesem Verfahren der Aufwand erheblich. Schwer zugängliche Geräte können ohne Mehrkosten ausgelesen werden und Terminabsprachen mit den Nutzern entfallen.</p>
        </article>
        <article class="method">
          <h2>Fernauslesung / automatische Ablesung</h2>
          <p>Die bequemste Lösung: Die Verbrauchswerte der einzelnen Geräte werden zentral in einer Gebäudezentrale gespeichert und dann per GPRS-Modem an das WohnArcaplus Abrechnungssystem übermittelt. Das Betreten der gesamten Liegenschaft entfällt und so werden Zeit und Kosten eingespart. Die Fernauslesung bildet zudem die Grundlage für weitere künftige Services wie z.B. das Energiedatenmanagement. Sie verfügen jederzeit über tagesaktuelle Verbrauchswerte und etwaige Gerätestörungen werden sofort gemeldet.</p>
        </article>
      </div>

      <figure class="method-visual visual--manual" style="margin:0">
        <div class="visual-area" role="img" aria-label="Illustration: Mitarbeiter liest Zähler in einem Mehrfamilienhaus vor Ort ab"></div>
        <figcaption class="caption">Mitarbeiter<br>vor Ort<br>vor jedem Zähler</figcaption>
      </figure>
      <figure class="method-visual visual--walkby" style="margin:0">
        <div class="visual-area" role="img" aria-label="Illustration: Mitarbeiter liest Zähler per Funk vor dem Haus aus"></div>
        <figcaption class="caption">Mitarbeiter<br>vor Ort<br>Funkauslesung<br>(Walk-by)</figcaption>
      </figure>
      <figure class="method-visual visual--remote" style="margin:0">
        <div class="visual-area" role="img" aria-label="Illustration: Mitarbeiter im Büro empfängt Zählerdaten per GSM"></div>
        <figcaption class="caption">Mitarbeiter<br>im Büro<br>Fernauslesung</figcaption>
      </figure>

      <div class="benefits methods-benefits">
        <h3>Ihre Vorteile:</h3>
        <ul>
          <li>Sichere Einhaltung aller Ablesetermine</li>
          <li>Hohe Datenqualität durch Plausibilitätsprüfung</li>
          <li>Funktionsprüfung und Wartung aller Geräte</li>
          <li>Vermeidung potenzieller Fehlerquellen bei der Übertragung der Verbrauchswerte in elektronischer Form</li>
          <li>Hohe Datenqualität für mehr Rechtssicherheit gegenüber den Nutzern</li>
        </ul>
      </div>
    </div>
  </section>

</div>
</body>
</html>
```